Tranquil Glide Door Product info

Need a catalog designed. 4 -6 pages
We are a commercial sliding door company.
Primary product is a barn door
35 STC Rating (sound rating)
see our web pages listed below
www.tranquilglidedoor-example.com
www.quickrailstock-example.com
Our product is gaining huge strides throughout the medical and hospitality sectors.
this is a 4- 6 page catalogue / brochure . Our product is currently used in many places but we also are creating new markets in the office space.
Updates

Target Market(s)

Commercial Architects , designers , Contractors .
Hospitals , high end hotels , Commercial building planners

Industry/Entity Type

Construction Company

Font styles to use
Serif

Requirements
Must have
• Selling points as to why our product is superior, good flow from concept to end. catch the eye of a designer . technical info . info on sound rating , Good photos, will provide better photos.
Nice to have
• see website from meridan doors and see ideas
Should not have
• too much writing

```html
<!DOCTYPE html>
<html lang="en">
<head>
<meta charset="UTF-8">
<title>Tranquil Glide Door – About Us &amp; Hardware</title>
<link href="https://fonts.googleapis.com/css2?family=Open+Sans:wght@300;400;600;700&display=swap" rel="stylesheet">
<style>
  :root {
    --brand-blue: #2f679c;
    --slate: #3f4a63;
    --panel-slate: #5b6885;
    --page-white: #f3f4f8;
    --ink: #2a2f3a;
    --white: #ffffff;
    --photo-wood: #9a6a3c;
    --photo-grey: #b9bcc6;
  }
  * { box-sizing: border-box; margin: 0; padding: 0; }
  html, body { width: 1200px; height: 789px; overflow: hidden; }
  body {
    font-family: "Open Sans", Arial, sans-serif;
    background: #a9cfd6;
    color: var(--ink);
  }
  .spread { display: flex; width: 1200px; height: 789px; }
  .page { position: relative; width: 600px; height: 789px; overflow: hidden; }

  /* Left page */
  .page--about { background: var(--page-white); }
  .lobby-photo {
    height: 280px;
    background: linear-gradient(160deg, #d7d9de 0%, #b49064 45%, var(--photo-wood) 65%, #5a5e66 100%);
  }
  .section-head {
    display: flex; align-items: center; gap: 16px;
    margin: 16px 0 8px;
  }
  .section-head__bar { height: 10px; background: var(--brand-blue); flex: 1; }
  .section-head__title { font-weight: 300; font-size: 28px; line-height: 1.3; color: var(--ink); }
  .about-text {
    width: 520px; margin: 0 auto;
    font-size: 13px; line-height: 1.45; text-align: center;
  }
  .superior-title {
    font-weight: 700; font-size: 21px; line-height: 1.3; text-align: center;
    margin: 16px 0 12px;
  }
  .markets { display: flex; gap: 8px; padding: 0 14px; }
  .market { flex: 1; min-width: 0; }
  .market__tab {
    display: block; padding: 6px 10px;
    color: var(--white); font-weight: 700; font-size: 13px; line-height: 1.3;
    white-space: nowrap;
    clip-path: polygon(0 0, 92% 0, 100% 100%, 0 100%);
  }
  .market__tab--blue { background: var(--brand-blue); }
  .market__tab--slate { background: var(--slate); }
  .market__text {
    font-size: 10px; line-height: 1.4; text-align: left;
    padding: 10px 4px 0;
  }

  /* Right page */
  .page--hardware { background: var(--page-white); }
  .hardware-panel {
    height: 410px; background: var(--panel-slate);
    color: var(--white); padding: 30px 36px;
  }
  .hardware-panel__label {
    display: inline-block; background: var(--white);
    color: var(--brand-blue); font-weight: 700; font-size: 22px;
    padding: 4px 40px 4px 46px; margin-left: -36px;
  }
  .hardware-panel__lead { font-weight: 700; font-size: 15px; margin: 16px 0 12px; }
  .hardware-list { list-style: none; font-size: 12.5px; line-height: 1.5; }
  .hardware-list li { position: relative; padding-left: 22px; }
  .hardware-list li::before {
    content: ""; position: absolute; left: 4px; top: 4px;
    width: 5px; height: 9px;
    border: solid var(--white); border-width: 0 2px 2px 0;
    transform: rotate(40deg);
  }
  .hardware-panel__text { font-size: 12.5px; line-height: 1.5; margin-top: 18px; }
  .hardware-photo {
    height: 379px;
    background: linear-gradient(135deg, #c9ccd4 0%, var(--photo-grey) 40%, #7d808a 60%, #6a4a33 100%);
  }
</style>
</head>
<body>
<main class="spread">
  <section class="page page--about">
    <div class="lobby-photo" role="img" aria-label="Photo of a modern building lobby with wood-clad columns and a sliding door"></div>

    <div class="section-head">
      <span class="section-head__bar"></span>
      <h2 class="section-head__title">About Us</h2>
      <span class="section-head__bar"></span>
    </div>
    <p class="about-text">Our mission is to provide a space saving solution without sacrificing performance or design. Our product not only looks great, but performs! Finally there is a good solution for the faults of sliding doors! No sight lines, lever and key lockable, gasketed and even STC and NIC rated with field and lab tests! Our knowledgeable staff is ready to help address all your needs! Contact us today for inquiries.</p>

    <h2 class="superior-title">why our product is superior</h2>

    <div class="markets">
      <article class="market">
        <h3 class="market__tab market__tab--blue">Health Care</h3>
        <p class="market__text">Lever lockable, key lockable, or push button for privacy. Privacy indicator available. Sealed from sight lines. With an STC and NIC rating, these doors are perfect for exam rooms and will help maximize floor space. Our concealed floor guide won't get in the way of rolling carts! Our door can even be taken down in emergency, similar to rescue hardware.</p>
      </article>
      <article class="market">
        <h3 class="market__tab market__tab--slate">Hospitality</h3>
        <p class="market__text">Privacy lockable and sealed from sight lines for bathroom application. Great for use on closets, or bedroom suite doors. We also offer a bi-parting system, perfect for any application.</p>
      </article>
      <article class="market">
        <h3 class="market__tab market__tab--blue">Office Interiors</h3>
        <p class="market__text">We believe our product is so great, we have it on our own office doors! Key or privacy lockable for security. Sound sealed for those conference calls or days when you need some peace and quiet! Space saving and looks great!</p>
      </article>
      <article class="market">
        <h3 class="market__tab market__tab--slate">Home Use</h3>
        <p class="market__text">Great for use in a high end home or apartment. Perfect for any interior home door. Our bi-parting system is perfect for those larger openings! Our system is easy to retrofit to suit your existing opening and your needs.</p>
      </article>
    </div>
  </section>

  <section class="page page--hardware">
    <div class="hardware-panel">
      <h2 class="hardware-panel__label">Hardware</h2>
      <p class="hardware-panel__lead">We offer a wide range of hardware to meet your specific needs:</p>
      <ul class="hardware-list">
        <li>Flush pulls</li>
        <li>Ladder pulls</li>
        <li>Custom pulls</li>
        <li>Key lockable mortise locks</li>
        <li>Thumb turn locks with or without privacy indicator</li>
        <li>Push button locks for privacy</li>
        <li>Latching, non-locking handles</li>
        <li>Auto door bottoms</li>
        <li>So much more! Tell us your application and we will find the perfect hardware for you.</li>
      </ul>
      <p class="hardware-panel__text">Our standard hardware consists of a backer plate, box track, fascia, receiving channel, felt gasketing, and a concealed floor guide. Find the handle or pull you want, or ask us to help! Our system is versatile and fully customizable. If we don't offer something for your needs, let us know and we will work with you to find the best solution.</p>
    </div>
    <div class="hardware-photo" role="img" aria-label="Close-up render of the sliding door track, roller carriage and wood door panel"></div>
  </section>
</main>
</body>
</html>
```